OREV - Helping People with Disabilities

OREV is a nonprofit that strives to enable people with physical disabilities to live meaningful, quality lives. OREV needs a professional attractive website that:
• establishes a strong brand image
• presents Orev's services to those who need it
• raises funds from potential donors
Please see WORD DOC attached for more information about design vision.

Target Market(s)

people with disabilities

Industry/Entity Type

charity website

Number of Pages Required

2 page

Font styles to use
Sans Serif

Requirements
Must have
• 1. 2 pages means 1 design for homepage and 1 design for top of inner pages (banner ideas)
Nice to have
• please see attached design brief (WORD DOC)

```html
<!DOCTYPE html>
<html lang="en">
<head>
<meta charset="utf-8">
<title>OREV – Helping People with Disabilities</title>
<link href="https://fonts.googleapis.com/css2?family=Roboto:wght@300;400;500;700;900&display=swap" rel="stylesheet">
<style>
:root{
  --teal:#0a6b6b;
  --teal-dark:#075a5b;
  --green:#2fb54a;
  --green-bright:#3cc55a;
  --ink:#111;
  --muted:#777;
  --line:#e6e6e6;
  --white:#fff;
}
*{box-sizing:border-box;margin:0;padding:0}
html,body{width:1200px;height:4415px;overflow:hidden}
body{position:relative;font-family:'Roboto',sans-serif;color:var(--ink);background:var(--white)}
.abs{position:absolute}

/* header */
.topbar{top:0;left:0;width:1200px;height:89px;background:var(--white)}
.follow{right:110px;top:38px;display:flex;align-items:center;gap:9px;font-size:14px;font-weight:500}
.follow .sq{width:15px;height:15px;background:var(--teal);border-radius:2px}
.nav{top:89px;left:0;width:1200px;height:50px;background:var(--teal)}
.nav a{position:absolute;top:16px;color:var(--white);font-size:15px;text-decoration:none}
.brand{left:533px;top:0;width:134px;height:128px;background:var(--white);border-radius:0 0 22px 22px;display:flex;flex-direction:column;align-items:center;justify-content:center;gap:8px}
.brand .dot{width:38px;height:38px;border-radius:50%;background:var(--teal)}
.brand .name{font-size:26px;font-weight:900;color:var(--teal);letter-spacing:1px}

/* hero */
.hero{top:139px;left:0;width:1200px;height:557px;background:linear-gradient(100deg,#1e2a1e 0%,#3d4a2c 35%,#8a8560 60%,#5e6a3c 80%,#2b3420 100%)}
.hero-title{left:110px;font-size:46px;font-weight:900;line-height:64px;color:var(--white);text-transform:uppercase}
.btn{display:flex;align-items:center;justify-content:center;background:var(--green);color:var(--white);font-weight:700;text-transform:uppercase;font-size:14px;text-decoration:none}
.hero .btn{position:absolute;left:110px;top:365px;width:290px;height:41px;font-size:15px}

/* quick links */
.quick{top:775px;width:225px;height:241px;background:var(--white);box-shadow:0 2px 14px rgba(0,0,0,.1);text-align:center;padding:40px 20px 0}
.quick.teal{border-bottom:4px solid var(--teal)}
.quick.green{border-bottom:4px solid var(--green)}
.quick svg{display:block;margin:0 auto 20px}
.quick p{font-size:13px;line-height:26px;color:var(--muted)}

/* about */
.about-img{left:111px;top:1135px;width:441px;height:504px;background:linear-gradient(135deg,#a8b59a,#7b8572 40%,#c9a98a 70%,#6d6a62);box-shadow:0 2px 14px rgba(0,0,0,.15)}
.h2{font-size:38px;font-weight:900;text-transform:uppercase;color:var(--ink)}
.about-text{left:608px;top:1237px;width:482px;font-size:15px;line-height:31px;color:var(--muted)}
.about-text p+p{margin-top:31px}

/* band */
.band{top:1741px;left:0;width:1200px;height:351px;background:linear-gradient(90deg,var(--teal-dark),#0d7574 50%,var(--teal-dark));text-align:center}
.band h3{position:absolute;top:72px;left:0;width:1200px;color:var(--white);font-size:39px;font-weight:700;line-height:64px;text-transform:uppercase}
.band .btn{position:absolute;left:475px;top:224px;width:250px;height:41px}

/* offer */
.offer{top:2247px;width:228px;height:338px;background:var(--white);box-shadow:0 2px 14px rgba(0,0,0,.1);text-align:center}
.offer .ph{height:158px}
.offer h4{margin-top:20px;font-size:16px;font-weight:700;text-transform:uppercase;line-height:26px;padding:0 14px}
.offer p{margin-top:6px;font-size:13px;line-height:23px;color:var(--muted);padding:0 16px}

/* news */
.news{left:111px;width:460px;height:163px;background:var(--white);box-shadow:0 2px 14px rgba(0,0,0,.1)}
.news .ph{position:absolute;left:5px;top:6px;width:160px;height:152px}
.news h5{position:absolute;left:187px;top:24px;width:255px;font-size:13px;font-weight:700;line-height:23px;text-transform:uppercase}
.news p{position:absolute;left:187px;top:80px;width:230px;font-size:12px;line-height:20px;color:var(--muted)}
.map{left:626px;top:2748px;width:463px;height:549px;background:linear-gradient(160deg,#cfe3cf,#b9d8bf 45%,#d6e6cf 75%,#c4dcc6)}

/* contact */
.contact{top:3422px;left:0;width:1200px;height:692px;background:linear-gradient(90deg,#2ea947,var(--green-bright) 45%,#33b14d)}
.contact h3{position:absolute;top:70px;width:1200px;text-align:center;color:var(--white);font-size:39px;font-weight:700;text-transform:uppercase;letter-spacing:1px}
.field{position:absolute;background:var(--white);font-size:13px;color:#666;padding:18px 26px}
.contact .btn{position:absolute;left:514px;top:578px;width:172px;height:41px;background:var(--teal)}

/* footer */
.fcol h6{font-size:23px;font-weight:700;text-transform:uppercase;margin-bottom:18px}
.fcol p{font-size:13px;line-height:26px;color:#555}
.fcol b{color:var(--ink);font-weight:700}
.copy{left:134px;top:4370px;font-size:13px;color:#555}
.totop{left:1130px;top:4277px;width:44px;height:44px;border-radius:50%;background:var(--teal);display:flex;align-items:center;justify-content:center}
</style>
</head>
<body>

<header>
  <div class="abs topbar"></div>
  <div class="abs follow">Follow Us:<span class="sq"></span><span class="sq"></span><span class="sq"></span></div>
  <nav class="abs nav">
    <a style="left:112px">About</a>
    <a style="left:196px">Programs</a>
    <a style="left:305px">Rehabilitation &amp; Sports</a>
    <a style="left:766px">Rights Realization</a>
    <a style="left:931px">News</a>
    <a style="left:1012px">Contact Us</a>
  </nav>
  <div class="abs brand"><span class="dot"></span><span class="name">OREV</span></div>
</header>

<section class="abs hero" role="img" aria-label="Girl running with open arms toward a smiling woman in a wheelchair on a sunny path">
  <h1 class="abs hero-title" style="top:144px">A good life for<br>everyone, like<br>everyone</h1>
  <a class="btn">Donate to help us help them</a>
</section>

<section>
  <div class="abs quick teal" style="left:111px">
    <svg width="56" height="60" viewBox="0 0 56 60" fill="none" stroke="#0a6b6b" stroke-width="3"><circle cx="20" cy="8" r="6"/><path d="M20 16v20l-8 20M20 36l8 20M20 22l14 6M34 28v28M44 28v28M34 28h10"/></svg>
    <p>I want to know What are all the rights available to people with physical disabilities and their families</p>
  </div>
  <div class="abs quick green" style="left:362px">
    <svg width="60" height="60" viewBox="0 0 60 60" fill="none" stroke="#2fb54a" stroke-width="3"><rect x="10" y="14" width="40" height="28" rx="2"/><path d="M4 46h52l-4 6H8zM20 26l10-5 10 5-10 5zM26 29v5h8v-5"/></svg>
    <p>I want to know Where I can join online classes offered by OREV</p>
  </div>
  <div class="abs quick teal" style="left:614px">
    <svg width="60" height="60" viewBox="0 0 60 60" fill="none" stroke="#0a6b6b" stroke-width="3"><circle cx="28" cy="8" r="6"/><path d="M28 16v18h14l6 14M20 26a16 16 0 1 0 22 20"/></svg>
    <p>I want to know What services there are for children with disabilities</p>
  </div>
  <div class="abs quick green" style="left:864px">
    <svg width="60" height="60" viewBox="0 0 60 60" fill="none" stroke="#2fb54a" stroke-width="3"><circle cx="20" cy="8" r="6"/><circle cx="40" cy="8" r="6"/><path d="M20 16v40M40 16v40M10 22h40M10 22v20M50 22v20"/></svg>
    <p>I want to know If there is a rehabilitation center in my area</p>
  </div>
</section>

<section>
  <div class="abs about-img" role="img" aria-label="Smiling boy in a wheelchair playing with building blocks alongside a carer"></div>
  <h2 class="abs h2" style="left:608px;top:1153px">About Us</h2>
  <div class="abs about-text">
    <p>On the other hand, we denounce with righteous indignation and dislike men who are so beguiled and demoralized by the charms of pleasure of the moment, so blinded by desire, that they cannot foresee the pain and trouble that are bound to ensue; and equal blame belongs to those who fail in their duty through weakness of will, which is the same as saying through shrinking from toil and pain.</p>
    <p>These cases are perfectly simple and easy to distinguish. In a free hour, when our power of choice is untrammelled and when nothing prevents our being able to do what we like best</p>
  </div>
  <a class="abs btn" style="left:608px;top:1570px;width:129px;height:43px">Read More</a>
</section>

<section class="abs band">
  <h3>Even people with disabilities can be with<br>everyone, like everyone</h3>
  <a class="btn">Don't leave them behind</a>
</section>

<section>
  <h2 class="abs h2" style="left:0;width:1200px;text-align:center;top:2158px">What We Offer</h2>
  <div class="abs offer" style="left:111px"><div class="ph" role="img" aria-label="Child in a wheelchair playing with toys in a classroom" style="background:linear-gradient(135deg,#5a9ad0,#d8553f 50%,#e8c65a)"></div><h4>Education</h4><p>OREV works to impart education and knowledge to people with disabilities and operates the dedicated campus</p></div>
  <div class="abs offer" style="left:361px"><div class="ph" role="img" aria-label="Wheelchair athletes playing basketball" style="background:linear-gradient(135deg,#e8e4de,#9a8c80 55%,#4d4540)"></div><h4>Sports and Rehab</h4><p>OREV encourages people with disabilities to play sports and find new strengths in themselves...</p></div>
  <div class="abs offer" style="left:611px"><div class="ph" role="img" aria-label="Man in a wheelchair working at an office desk" style="background:linear-gradient(135deg,#c9d2d8,#6f7d88 55%,#3e4852)"></div><h4>Rights Realization</h4><p>OREV promotes policies concerning people with physical-motor disabilities, promotes their rights, ...</p></div>
  <div class="abs offer" style="left:861px"><div class="ph" role="img" aria-label="Two women embracing beside a car" style="background:linear-gradient(135deg,#7d7a74,#b9a898 50%,#55534f)"></div><h4>Community<br>Infrastructure</h4><p>OREV owns the association's houses all over the country, rehabilitation day centers,...</p></div>
</section>

<section>
  <h2 class="abs h2" style="left:110px;top:2674px">News</h2>
  <h2 class="abs h2" style="left:626px;top:2674px">Map of Branches</h2>
  <article class="abs news" style="top:2748px"><div class="ph" role="img" aria-label="Child in a wheelchair playing ball outdoors" style="background:linear-gradient(135deg,#4f8a3a,#d8c84a 50%,#c44a5a)"></div><h5>Sed ut perspiciatis unde omnis iste natus error sit olupta</h5><p>Sed ut perspiciatis unde omnis iste natus error sit voluptatem accusantium doloremque laudantium,</p></article>
  <article class="abs news" style="top:2940px"><div class="ph" role="img" aria-label="Carer helping an elderly woman walk indoors" style="background:linear-gradient(135deg,#d9cfc4,#8a6e62 50%,#c9b7a4)"></div><h5>Sed ut perspiciatis unde omnis iste natus error sit olupta</h5><p>Sed ut perspiciatis unde omnis iste natus error sit voluptatem accusantium doloremque laudantium,</p></article>
  <article class="abs news" style="top:3132px"><div class="ph" role="img" aria-label="Group meeting around a table in a bright office" style="background:linear-gradient(135deg,#e4e6e8,#8d959c 50%,#4a5058)"></div><h5>Sed ut perspiciatis unde omnis iste natus error sit olupta</h5><p>Sed ut perspiciatis unde omnis iste natus error sit voluptatem accusantium doloremque laudantium,</p></article>
  <div class="abs map" role="img" aria-label="Map of branch locations across the central United States"></div>
</section>

<section class="abs contact">
  <h3>Get in touch with us</h3>
  <div class="field" style="left:187px;top:180px;width:391px;height:51px">First Name</div>
  <div class="field" style="left:622px;top:180px;width:390px;height:51px">Last Name</div>
  <div class="field" style="left:187px;top:262px;width:391px;height:51px">Email Address</div>
  <div class="field" style="left:622px;top:262px;width:390px;height:51px">Contact Number</div>
  <div class="field" style="left:187px;top:343px;width:825px;height:197px">Type Your Message Here.....</div>
  <a class="btn">Send Message</a>
</section>

<footer>
  <div class="abs fcol" style="left:134px;top:4190px;width:330px">
    <h6>About Company</h6>
    <p>I must explain to you how all this mistaken idea of denouncing pleasure and praising pain was born and I will give you a complete account of the system, and expound the actual</p>
  </div>
  <div class="abs fcol" style="left:586px;top:4190px;width:240px">
    <h6>Contact Details</h6>
    <p><b>Tel :</b> +1 555 014 2270<br><b>Email :</b> hello@orevcare.org<br><b>Address :</b> 22y, Orev lorem lipsum is<br>876 543</p>
  </div>
  <div class="abs fcol" style="left:938px;top:4190px;width:160px">
    <h6>Follow Us</h6>
    <p>Friendbook<br>Snapgram<br>WorkLink<br>Chirper</p>
  </div>
  <div class="abs totop"><svg width="20" height="20" viewBox="0 0 20 20" fill="none" stroke="#fff" stroke-width="2.5"><path d="M10 17V4M4 9l6-6 6 6"/></svg></div>
  <div class="abs copy">(c) Copyright 2023 | All Rights Reserved.</div>
</footer>

</body>
</html>
```